Advertisement Design

I'm looking for a post card sized advertisement piece that I will be dropping off to commercial and residential customers.
On one side I want it promoting carpet cleaning services and on the other side dryer vent cleaning services.
I've uploaded two different layouts of my company logo for you to choice from.
One batch will be printed with my Michigan Number
One batch will be printed with my Tennessee number
Will share contact numbers with the winner so just use a make up number
555-318-4729

```html
<!DOCTYPE html>
<html lang="en">
<head>
<meta charset="utf-8">
<title>Fernleaf Postcards – Carpet &amp; Dryer Vent Cleaning</title>
<link rel="stylesheet" href="https://fonts.googleapis.com/css2?family=Poppins:wght@400;500;600;700;800&family=Roboto+Condensed:wght@500;700&display=swap">
<style>
  :root {
    --blue: #0b77bf;
    --blue-dark: #0a5f9a;
    --ink: #151515;
    --slate: #4b4c4f;
    --page: #f1f1f1;
    --white: #ffffff;
    --rule: #cfcfcf;
  }
  * { box-sizing: border-box; margin: 0; padding: 0; }
  html, body { width: 1200px; height: 929px; overflow: hidden; }
  body { background: var(--page); font-family: "Poppins", sans-serif; color: var(--ink); position: relative; }

  .postcard { position: absolute; width: 606px; height: 404px; background: var(--white); overflow: hidden; }
  .postcard--carpet { left: 298px; top: 56px; }
  .postcard--vent { left: 296px; top: 484px; }

  .corner-block { position: absolute; right: 0; top: 0; width: 106px; height: 182px; background: var(--slate); }

  .brand { position: absolute; display: flex; align-items: center; gap: 9px; }
  .brand__mark { width: 33px; height: 33px; background: var(--blue); border-radius: 4px; }
  .brand__divider { width: 2px; height: 57px; background: var(--slate); }
  .brand__name { font-family: "Poppins", sans-serif; font-weight: 600; font-size: 15px; color: var(--blue); line-height: 1.1; }
  .postcard--carpet .brand { left: 34px; top: 17px; }
  .postcard--vent .brand { left: 29px; top: 17px; }

  .photo { position: absolute; border: 3px solid var(--white); box-shadow: 0 0 0 1.5px #d8e6f2; }
  .photo--carpet { left: 324px; top: 17px; width: 242px; height: 240px; border-radius: 22px;
    background: linear-gradient(145deg, #2e6ea8 0%, #8a857d 45%, #6d6a66 60%, #0d5d9e 100%); }
  .photo--vent { left: 356px; top: 26px; width: 222px; height: 182px; border-radius: 12px;
    background: linear-gradient(135deg, #c7b08a 0%, #d9c9a8 40%, #e8e6e0 60%, #6d89b5 100%); }

  .headline { position: absolute; }
  .headline--carpet { left: 32px; top: 74px; }
  .headline--vent { left: 28px; top: 82px; }

  .services-band { position: absolute; left: 32px; top: 173px; width: 250px; height: 31px; background: var(--slate);
    color: var(--white); font-family: "Poppins", sans-serif; font-weight: 500; font-size: 25px; letter-spacing: 12.5px;
    display: flex; align-items: center; justify-content: center; padding-left: 12px; line-height: 1; }

  .intro { position: absolute; left: 34px; top: 210px; width: 250px; font-size: 9.6px; line-height: 12px; font-weight: 600; }
  .intro__lead { color: var(--blue); font-weight: 700; }

  .offer-strip { position: absolute; left: 21px; top: 279px; width: 562px; height: 61px; background: var(--blue);
    border-radius: 8px; display: flex; }
  .offer { position: relative; flex: 1 1 auto; display: flex; flex-direction: column; align-items: center;
    justify-content: flex-end; padding-bottom: 15px; color: var(--white); font-size: 8.6px; font-weight: 600;
    line-height: 11px; text-align: center; }
  .offer + .offer { border-left: 1px solid rgba(255,255,255,0.25); }
  .offer__icon { position: absolute; top: -12px; left: 50%; transform: translateX(-50%); width: 30px; height: 30px;
    background: #8b8d91; border: 2px solid var(--white); border-radius: 8px; }
  .offer:nth-child(1) { width: 89px; }
  .offer:nth-child(2) { width: 89px; }
  .offer:nth-child(3) { width: 53px; }
  .offer:nth-child(4) { width: 116px; }
  .offer:nth-child(5) { width: 99px; }
  .offer:nth-child(6) { width: 106px; }

  .contact-row { position: absolute; left: 21px; right: 21px; display: flex; justify-content: space-between; align-items: center; }
  .postcard--carpet .contact-row { top: 352px; }
  .postcard--vent .contact-row { top: 355px; left: 29px; right: 24px; }
  .contact { display: flex; align-items: center; gap: 7px; font-size: 15px; font-weight: 600; color: var(--ink); line-height: 1; }
  .contact svg { width: 17px; height: 17px; flex: none; }

  .vent-rule { position: absolute; left: 29px; top: 159px; width: 305px; height: 1px; background: var(--rule); }
  .vent-tagline { position: absolute; left: 29px; top: 171px; width: 300px; font-size: 13.6px; line-height: 16px; font-weight: 600; color: var(--blue); }

  .howto { position: absolute; left: 29px; top: 221px; width: 550px; height: 121px; background: var(--blue); border-radius: 10px; color: var(--white); }
  .howto__intro { position: absolute; left: 21px; top: 15px; width: 205px; }
  .howto__title { font-size: 10.6px; font-weight: 700; line-height: 13px; margin-bottom: 3px; }
  .howto__text { font-size: 9.3px; font-weight: 400; line-height: 11.9px; }
  .howto__divider { position: absolute; left: 248px; top: 18px; width: 1px; height: 88px; background: rgba(255,255,255,0.45); }
  .howto__steps { position: absolute; left: 271px; top: 15px; list-style: none; }
  .howto__steps li { font-size: 9.9px; font-weight: 600; line-height: 12px; margin-bottom: 6.6px; }
</style>
</head>
<body>

<section class="postcard postcard--carpet">
  <div class="corner-block"></div>
  <div class="photo photo--carpet" role="img" aria-label="Photo of a vacuum cleaner head on a carpet"></div>

  <div class="brand">
    <span class="brand__mark"></span>
    <span class="brand__divider"></span>
    <span class="brand__name">Fernleaf<br>Property Services</span>
  </div>

  <svg class="headline headline--carpet" width="260" height="100" viewBox="0 0 260 100" aria-label="Carpet Cleaning">
    <text x="0" y="93" fill="var(--blue)" font-family="Roboto Condensed, sans-serif" font-weight="700" font-size="126" textLength="44" lengthAdjust="spacingAndGlyphs">C</text>
    <text x="50" y="52" fill="var(--blue)" font-family="Roboto Condensed, sans-serif" font-weight="700" font-size="64" textLength="198" lengthAdjust="spacingAndGlyphs">ARPET</text>
    <text x="48" y="93" fill="var(--ink)" font-family="Roboto Condensed, sans-serif" font-weight="700" font-size="51" textLength="204" lengthAdjust="spacingAndGlyphs">LEANING</text>
  </svg>

  <div class="services-band">SERVICES</div>

  <p class="intro"><span class="intro__lead">WE HAVE BEEN PROVIDING CARPET CLEANING SERVICES FOR 40 YEARS.</span> With state-of-the-art industrial equipment &amp; out years of experience there is not mush we cannot get clean.</p>

  <div class="offer-strip">
    <div class="offer"><span class="offer__icon"></span>Industrial<br>Carpet Cleaning</div>
    <div class="offer"><span class="offer__icon"></span>Residential<br>Carpet Cleaning</div>
    <div class="offer"><span class="offer__icon"></span>Rug<br>Cleaning</div>
    <div class="offer"><span class="offer__icon"></span>Boat, RV, Private Plane<br>Carpet Cleaning</div>
    <div class="offer"><span class="offer__icon"></span>Tile &amp; Grout steam<br>cleaning / sealing</div>
    <div class="offer"><span class="offer__icon"></span>Corridor &amp; Outdoor<br>Carpet Cleaning</div>
  </div>

  <div class="contact-row">
    <span class="contact">
      <svg viewBox="0 0 24 24"><path fill="var(--blue)" d="M6.6 2.5l3 3.4-1.9 2.6c1.3 2.8 3.4 5 6.2 6.4l2.6-1.9 3.4 3-1.9 3.4C11 19 4.8 12.8 3.3 4.4z"/></svg>
      555-318-4729
    </span>
    <span class="contact">
      <svg viewBox="0 0 24 24"><rect x="2" y="5" width="20" height="14" fill="none" stroke="var(--blue)" stroke-width="2"/><path d="M2 5l10 8 10-8" fill="none" stroke="var(--blue)" stroke-width="2"/></svg>
      BILLING@FERNLEAF.COM
    </span>
    <span class="contact">
      <svg viewBox="0 0 24 24" fill="none" stroke="var(--blue)" stroke-width="1.8"><circle cx="12" cy="12" r="10"/><ellipse cx="12" cy="12" rx="4.5" ry="10"/><path d="M2 12h20M4 6.5h16M4 17.5h16"/></svg>
      www.fernleaf.com
    </span>
  </div>
</section>

<section class="postcard postcard--vent">
  <div class="corner-block"></div>
  <div class="photo photo--vent" role="img" aria-label="Photo of a technician servicing a wall-mounted unit"></div>

  <div class="brand">
    <span class="brand__mark"></span>
    <span class="brand__divider"></span>
    <span class="brand__name">Fernleaf<br>Property Services</span>
  </div>

  <svg class="headline headline--vent" width="310" height="76" viewBox="0 0 310 76" aria-label="Dryer Vent Cleaning Services">
    <text x="0" y="37" fill="var(--blue)" font-family="Poppins, sans-serif" font-weight="800" font-size="46" textLength="260" lengthAdjust="spacingAndGlyphs">DRYER VENT</text>
    <text x="1" y="72" fill="var(--ink)" font-family="Poppins, sans-serif" font-weight="700" font-size="35" textLength="305" lengthAdjust="spacingAndGlyphs">CLEANING SERVICES</text>
  </svg>

  <div class="vent-rule"></div>
  <p class="vent-tagline">This laundry room maintenance trick will speed up drying time</p>

  <div class="howto">
    <div class="howto__intro">
      <h2 class="howto__title">HOW DO YOU CLEAN A DRYER VENT?</h2>
      <p class="howto__text">A DIY dryer vent cleaning process shouldn’t take you more than an hour as long as you have the right info and tools. Here are seven simple steps that will get all that lint and gunk out of the hose attachment.</p>
    </div>
    <div class="howto__divider"></div>
    <ol class="howto__steps">
      <li>Step 1: Gather your supplies</li>
      <li>Step 2: Disconnect the duct</li>
      <li>Step 3: Vacuum the entrance to the dryer vent</li>
      <li>Step 4: Connect the rods in a dryer duct cleaning kit</li>
      <li>Step 5. Turn on the drill</li>
    </ol>
  </div>

  <div class="contact-row">
    <span class="contact">
      <svg viewBox="0 0 24 24"><path fill="var(--blue)" d="M6.6 2.5l3 3.4-1.9 2.6c1.3 2.8 3.4 5 6.2 6.4l2.6-1.9 3.4 3-1.9 3.4C11 19 4.8 12.8 3.3 4.4z"/></svg>
      555-318-4729
    </span>
    <span class="contact">
      <svg viewBox="0 0 24 24"><rect x="2" y="5" width="20" height="14" fill="none" stroke="var(--blue)" stroke-width="2"/><path d="M2 5l10 8 10-8" fill="none" stroke="var(--blue)" stroke-width="2"/></svg>
      BILLING@FERNLEAF.COM
    </span>
    <span class="contact">
      <svg viewBox="0 0 24 24" fill="none" stroke="var(--blue)" stroke-width="1.8"><circle cx="12" cy="12" r="10"/><ellipse cx="12" cy="12" rx="4.5" ry="10"/><path d="M2 12h20M4 6.5h16M4 17.5h16"/></svg>
      www.fernleaf.com
    </span>
  </div>
</section>

</body>
</html>
```